Front cover of trifold brochure

This is for my real estate company. I need a design for the front page of the tri fold brochure. The interior of the brochure will constantly change, however I wanted to update the front cover to something more modern. I sell high end vacation homes on a Grand Lake, located in Northeast Oklahoma. So something that would appeal to vacation/second lake home buyers would be great. My logo colors are orange and burgundy, if we could incorporate those colors that would be great. I have attached a zip drive with all of the versions of my logo. I want to have a logo on there, as well as my phone number and my website. My website is www.tarlowandco.com, and my office number is 918-436-2091.

```html
<!DOCTYPE html>
<html lang="en">
<head>
<meta charset="utf-8">
<title>Tarlow &amp; Company Realty – Trifold Brochure</title>
<link rel="stylesheet" href="https://fonts.googleapis.com/css2?family=Cinzel:wght@400&family=Oswald:wght@300;400;500&family=Open+Sans:wght@400&display=swap">
<style>
  :root {
    --orange: #cd7f2c;
    --burgundy: #873551;
    --white: #ffffff;
    --ink: #1e1e1e;
    --backdrop: #cdd3d9;
    --lime: #d6e23a;
  }
  * { margin: 0; padding: 0; box-sizing: border-box; }
  html, body { width: 800px; height: 1200px; overflow: hidden; }
  body { background: var(--backdrop); position: relative; }

  .spread {
    position: absolute; left: 10px; top: 325px;
    width: 780px; height: 550px;
    box-shadow: 0 6px 18px rgba(0,0,0,.25);
    background: var(--white);
    overflow: hidden;
  }
  .spread-shapes { position: absolute; inset: 0; }

  .abs { position: absolute; }

  .body-copy {
    left: 14px; top: 40px; width: 232px;
    font: 400 8.3px/11px "Open Sans", sans-serif;
    color: var(--ink); text-align: justify;
  }
  .intro-copy {
    left: 17px; top: 477px; width: 232px;
    font: 400 14.5px/19px "Open Sans", sans-serif;
    color: var(--white); text-align: justify;
  }

  .contact {
    left: 260px; top: 28px; width: 260px; text-align: center;
    font-family: "Oswald", sans-serif; color: var(--white);
  }
  .contact-heading { font-weight: 500; font-size: 10.5px; letter-spacing: .2px; }
  .contact-line { font-weight: 300; font-size: 9.5px; line-height: 13px; opacity: .9; }
  .contact-phone { font-weight: 400; font-size: 17px; color: var(--orange); line-height: 22px; margin-top: 2px; }
  .contact-email { font-weight: 400; font-size: 10px; }

  .brand {
    display: flex; align-items: center; gap: 7px;
    font-family: "Cinzel", serif; font-weight: 400; color: var(--white);
  }
  .brand-mark { width: 14px; height: 14px; background: var(--orange); flex: none; }
  .brand-name { font-size: 17px; line-height: 19px; }
  .brand-name small { display: block; font-size: 11px; line-height: 14px; }
  .brand--panel { left: 320px; top: 300px; }
  .brand--cover { left: 598px; top: 50px; }
  .brand--cover .brand-mark { background: var(--burgundy); }

  .cover-phone {
    left: 540px; top: 360px; width: 230px;
    display: flex; align-items: center; justify-content: center; gap: 8px;
    font: 500 25px/1 "Oswald", sans-serif; color: var(--white);
  }
  .cover-title {
    left: 520px; top: 416px; width: 260px; text-align: center;
    font: 400 21px/28px "Cinzel", serif; color: var(--white); letter-spacing: 1.5px;
  }
  .web {
    font: 400 15px/40px "Oswald", sans-serif; color: var(--burgundy);
    text-align: center; top: 510px; height: 40px;
  }
  .web--panel { left: 260px; width: 260px; }
  .web--cover { left: 520px; width: 260px; }
</style>
</head>
<body>
<main class="spread">
  <svg class="spread-shapes" width="780" height="550" viewBox="0 0 780 550" aria-hidden="false">
    <!-- inside panel -->
    <rect x="0" y="234" width="260" height="182" fill="#6aa6c4" role="img" aria-label="Photo of a resort pool with white umbrellas and red-roofed villas by the lake"/>
    <path d="M0 424 L230 340 Q255 332 260 350 L260 550 L0 550 Z" fill="var(--orange)"/>

    <!-- contact panel -->
    <rect x="260" y="0" width="260" height="550" fill="var(--burgundy)"/>
    <defs>
      <linearGradient id="sunset" x1="0" y1="0" x2="0" y2="1">
        <stop offset="0" stop-color="#4a4860"/>
        <stop offset=".45" stop-color="#e07a5a"/>
        <stop offset="1" stop-color="#2b2430"/>
      </linearGradient>
      <linearGradient id="golf" x1="0" y1="0" x2="0" y2="1">
        <stop offset="0" stop-color="#8fb8d8"/>
        <stop offset=".45" stop-color="#4d7a38"/>
        <stop offset="1" stop-color="#1d3040"/>
      </linearGradient>
      <linearGradient id="clubhouse" x1="0" y1="0" x2="0" y2="1">
        <stop offset="0" stop-color="#5d92d2"/>
        <stop offset=".55" stop-color="#b89b7a"/>
        <stop offset="1" stop-color="#4f8a34"/>
      </linearGradient>
    </defs>
    <circle cx="386" cy="191" r="62" fill="url(#clubhouse)" role="img" aria-label="Round photo of a lakeside clubhouse on a green lawn"/>
    <rect x="260" y="403" width="260" height="107" fill="url(#sunset)" role="img" aria-label="Photo of a sunset over the lake with bare trees and docks"/>
    <rect x="0" y="510" width="780" height="40" fill="var(--orange)"/>
    <rect x="0" y="424" width="260" height="126" fill="none"/>

    <!-- cover panel -->
    <rect x="520" y="140" width="260" height="263" fill="url(#golf)" role="img" aria-label="Photo of a lakeside golf green with trees reflected in the water"/>
    <path d="M478 0 L780 0 L780 143 L540 215 Q522 220 520 205 L520 95 Z" fill="var(--orange)"/>
    <rect x="520" y="403" width="260" height="107" fill="var(--burgundy)"/>
    <rect x="520" y="510" width="260" height="40" fill="var(--orange)"/>
  </svg>

  <p class="abs body-copy">This is Photoshop's version of Lorem Ipsum. Proin gravida nibh vel velit auctor aliquet. Aenean sollicitudin, lorem quis bibendum auctor, nisi elit consequat ipsum, nec sagittis sem nibh id elit. Duis sed odio sit amet nibh vulputate cursus a sit amet mauris. Morbi accumsan ipsum velit. Nam nec tellus a odio tincidunt auctor a ornare odio. Sed non mauris vitae erat consequat auctor eu in elit. Class aptent taciti sociosqu ad litora torquent per conubia nostra, per inceptos himenaeos. Mauris in erat justo. Nullam ac urna eu felis dapibus condimentum sit amet a augue. Sed non neque elit. Sed ut imperdiet nisi. Proin condimentum fermentum nunc. Etiam pharetra, erat sed fermentum feugiat, velit mauris egestas quam, ut aliquam massa nisl quis neque. Suspendisse in orci enim.</p>
  <p class="abs intro-copy">This is Photoshop's version of Lorem Ipsum. Proin gravida nibh vel velit auctor aliquet. Aenean</p>

  <section class="abs contact">
    <h2 class="contact-heading">WE WOULD LOVE TO HEAR FROM YOU!</h2>
    <p class="contact-line">Send us a message and we'll get right back in touch.</p>
    <p class="contact-line">Tarlow &amp; Company Realty</p>
    <p class="contact-phone">918.436.2050</p>
    <p class="contact-email">dana@tarlowandco.net</p>
  </section>

  <div class="abs brand brand--panel">
    <span class="brand-mark"></span>
    <span class="brand-name">Tarlow<small>&amp; Company Realty</small></span>
  </div>
  <p class="abs web web--panel">www.tarlowandco.com</p>

  <div class="abs brand brand--cover">
    <span class="brand-mark"></span>
    <span class="brand-name">Tarlow<small>&amp; Company Realty</small></span>
  </div>
  <div class="abs cover-phone">
    <svg width="22" height="22" viewBox="0 0 24 24" aria-hidden="true"><path fill="var(--orange)" d="M6.6 10.8a15.1 15.1 0 0 0 6.6 6.6l2.2-2.2c.3-.3.7-.4 1-.2 1.1.4 2.3.6 3.6.6.6 0 1 .4 1 1V20c0 .6-.4 1-1 1A17 17 0 0 1 3 4c0-.6.4-1 1-1h3.5c.6 0 1 .4 1 1 0 1.3.2 2.5.6 3.6.1.3 0 .7-.2 1z"/></svg>
    <span>918-436-2091</span>
  </div>
  <h1 class="abs cover-title">GRAND LAKE<br>WATERFRONT<br>PROPERTY</h1>
  <p class="abs web web--cover">www.tarlowandco.com</p>
</main>
</body>
</html>
```